WP website design (Brisko)

We need a wordpress design that will incorporate a professional color scheme with company logo in a clean layout. The design needs to consider that this will be developed on a responsive theme. Colors are that of the logo and and an accent color (perhaps light brown/tan). Client wants a 'modern' look.

Industry/Entity Type

It Company

Font styles to use
Serif
Sans Serif

Colors

Designer to choose colors to be used in the design.

Requirements
Must have
• Must Have:
- Navigation: 1) Home 2) Real Estate Listings 3) Auctions 4) Buyers 5) Sellers 6) Services 7) Meet the Crew 8) Contact Us

Site will have a slideshow element (image attached) and the following widgets: 1) Featured Auctions 2) Testimonials blog widget 3) 'Auction Alerts' email sign up 4) FB Twitter RSS.

In the footer, there will be smaller company logo, the affiliations logo, and contact info below:
Brisko Auctions & Realty, Inc.
58391 Corvan Hollow Road • Suite 604 • Orlando, FL 32899
Office: 407.555.0148 / Cell: 407.555.0193 / Fax: 407.555.0176
Email: info@briskoauctions.example
Nice to have
• - - Site will have drop-down menus - please indicate the styling, for instance the dropdown menus 1) Upcoming Auctions 2) Past Auctions under the 'Auctions' link

```html
<!DOCTYPE html>
<html lang="en">
<head>
<meta charset="utf-8">
<title>Brisko Auctions</title>
<link rel="stylesheet" href="https://fonts.googleapis.com/css2?family=Roboto+Slab:wght@400&family=Arimo:wght@400;700&family=Asap:wght@400&display=swap">
<style>
:root{
  --brand:#9b1e26;
  --ink:#222;
  --muted:#777;
  --line:#dcdcdc;
  --nav:#1f1f1f;
  --footer:#070707;
  --price:#1a9a3a;
  --field:#4a4a4a;
  --white:#fff;
}
*{box-sizing:border-box;margin:0;padding:0}
html,body{width:1092px;height:1200px;overflow:hidden;background:var(--white)}
body{position:relative;font-family:"Arimo",Arial,sans-serif;color:var(--ink)}
.abs{position:absolute}

.site-header{left:0;top:0;width:1092px;height:125px}
.brand-mark{left:0;width:1092px;top:44px;text-align:center;font-family:"Roboto Slab",Georgia,serif;font-size:36px;color:var(--brand);letter-spacing:1px}

.main-nav{left:0;top:125px;width:1092px;height:38px;background:var(--nav)}
.main-nav ul{list-style:none;position:absolute;left:151px;top:0;display:flex;gap:16px;height:38px;align-items:center}
.main-nav li{font-family:"Roboto Slab",Georgia,serif;font-size:11.5px;color:var(--white);text-transform:uppercase;letter-spacing:-.2px}
.search{left:796px;top:9px;width:161px;height:22px;background:var(--white);border-radius:2px;font-size:10px;color:#555;padding:6px 8px}
.search svg{position:absolute;right:5px;top:4px}

.hero{left:0;top:163px;width:1092px;height:272px;overflow:hidden}
.hero-a{left:0;top:0;width:1092px;height:272px;background:linear-gradient(180deg,#9fc3e0 0%,#c9b79c 45%,#7d6b55 75%,#6f8a4c 100%);clip-path:polygon(0 0,570px 0,528px 272px,0 272px)}
.hero-b{left:0;top:0;width:1092px;height:272px;background:linear-gradient(180deg,#8fb4d8 0%,#cfd3d4 40%,#a9aaa6 70%,#5f7c43 100%);clip-path:polygon(570px 0,1092px 0,1092px 272px,528px 272px)}

.dropdown{left:308px;top:170px;width:126px;height:184px;background:rgba(255,255,255,.88);box-shadow:0 1px 3px rgba(0,0,0,.25);padding-top:14px}
.dropdown::before{content:"";position:absolute;top:-6px;left:36px;border:6px solid transparent;border-top:0;border-bottom-color:rgba(255,255,255,.88)}
.dropdown li{list-style:none;font-family:"Roboto Slab",Georgia,serif;font-size:9.5px;color:#444;padding-left:8px;height:27.6px;line-height:14px}
.dropdown li.active{color:var(--brand)}

.widget{left:136px;width:189px;border:1px solid var(--line);background:var(--white)}
.widget h3{margin:2px;height:29px;background:var(--brand);color:var(--white);font-family:"Roboto Slab",Georgia,serif;font-weight:400;font-size:12.5px;line-height:29px;padding-left:6px;text-transform:uppercase}
.testimonial{top:470px;height:202px}
.testimonial p{font-family:"Roboto Slab",Georgia,serif;font-size:10.5px;line-height:18.2px;color:#888;padding:10px 8px 0 10px}
.testimonial p::before{content:"\201C";font-size:22px;color:#aaa;vertical-align:-6px;margin-right:2px}
.view-all{position:absolute;right:10px;bottom:10px;font-size:10.5px;color:var(--brand)}
.alerts{top:691px;height:167px}
.alerts .note{font-size:9.5px;color:#444;padding:14px 0 0 9px}
.field{margin:14px 0 0 8px;width:171px;height:23px;background:var(--field);color:var(--white);font-size:9.5px;padding:7px 6px}
.field+.field{margin-top:4px}
.submit{margin:5px 0 0 8px;width:50px;height:23px;background:#000;color:var(--white);font-size:9.5px;line-height:23px;text-align:center}
.connect{top:875px;height:100px}
.social{display:flex;gap:4px;padding:18px 0 0 8px}
.social span{width:40px;height:40px;background:#555;border:1px solid #333;border-radius:2px}

.featured{left:340px;top:470px;width:618px;height:505px;border:1px solid var(--line)}
.tabs{display:flex;height:51px;border-bottom:1px solid var(--line)}
.tab{width:211px;border-right:1px solid var(--line);background:#fafafa;display:flex;align-items:center;padding-left:14px;gap:9px;font-family:"Roboto Slab",Georgia,serif;font-size:14.5px;color:#777;text-transform:uppercase}
.tab:first-child{width:212px;background:var(--white);color:var(--brand);border-bottom:1px solid var(--white);margin-bottom:-1px}
.tab:last-child{border-right:0;flex:1}
.tab svg{flex:none}
.listing{left:17px;width:584px;height:212px}
.listing.one{top:72px}
.listing.two{top:282px}
.listing.one::after{content:"";position:absolute;left:0;right:0;bottom:0;border-bottom:1px solid #e6e6e6}
.photo{left:0;top:0;width:219px;height:190px;border:5px solid #999;background:linear-gradient(180deg,#9ec3e6 0%,#d8dcdd 38%,#9d9f9c 62%,#c8c8c4 100%)}
.info{left:232px;top:13px;width:390px}
.info h4{font-family:"Arimo",Arial,sans-serif;font-weight:400;font-size:12.5px;color:var(--brand);text-transform:uppercase}
.info .lede{font-size:10.5px;line-height:13px;width:300px;margin:13px 0 8px 2px;color:#222}
.spec{display:flex;height:27.3px;align-items:center;border-bottom:1px solid #e3e3e3;width:353px;font-size:10.5px;padding-left:2px}
.spec .k{width:110px;color:#333}
.spec .c{width:31px}
.spec .v{color:#222}
.spec .v.price{color:var(--price)}
.actions{display:flex;gap:3px;margin:12px 0 0 2px}
.actions span{background:#000;color:var(--white);font-size:12px;height:24px;line-height:24px;padding:0 8px}

.site-footer{left:0;top:998px;width:1092px;height:202px;background:var(--footer);color:var(--white)}
.footer-mark{left:139px;top:38px;font-family:"Roboto Slab",Georgia,serif;font-size:22px;color:var(--brand)}
.footer-name{left:140px;top:95px;font-family:"Asap",Arial,sans-serif;font-size:16.5px}
.footer-contact{left:140px;top:120px;font-family:"Asap",Arial,sans-serif;font-size:11px;line-height:16.4px}
.badges{left:744px;top:59px;display:flex;gap:10px;align-items:center}
.badges span{background:#e8e8e8}
.copyright{left:752px;top:118px;font-family:"Asap",Arial,sans-serif;font-size:12px}
</style>
</head>
<body>
<header class="site-header abs">
  <div class="brand-mark abs">Brisko Auctions</div>
</header>

<nav class="main-nav abs">
  <ul>
    <li>Home</li><li>Real Estate Listings</li><li>Auctions</li><li>Buyers</li><li>Sellers</li><li>Services</li><li>Meet the Crew</li><li>Contact Us</li>
  </ul>
  <div class="search abs">Search
    <svg width="14" height="14" viewBox="0 0 14 14"><circle cx="5.5" cy="5.5" r="4" fill="none" stroke="#222" stroke-width="2"/><line x1="8.5" y1="8.5" x2="13" y2="13" stroke="#222" stroke-width="2.4"/></svg>
  </div>
</nav>

<section class="hero abs">
  <div class="hero-a abs" role="img" aria-label="Photo of a large Mediterranean-style villa with a fountain driveway"></div>
  <div class="hero-b abs" role="img" aria-label="Photo of a white stucco home with palm trees and paver driveway"></div>
</section>

<ul class="dropdown abs">
  <li>Upcoming Auctions</li><li>Past Auctions</li><li class="active">Upcoming Auctions &nbsp;›</li><li>Past Auctions</li><li>Upcoming Auctions</li><li>Past Auctions</li>
</ul>

<aside class="widget testimonial abs">
  <h3>Testimonial</h3>
  <p>Lorem ipsum dolor sit ullam corper als suscipit lobortis als consectetuer adipis cing elit, sed diam nonummy nibh euismod tincidunt ut laoreet dolore magna aliquam erat.</p>
  <span class="view-all">VIEW ALL</span>
</aside>

<aside class="widget alerts abs">
  <h3>Auction Alerts</h3>
  <div class="note">Enter Your Email For Newsletter Signup</div>
  <div class="field">Name</div>
  <div class="field">Email</div>
  <div class="submit">SUBMIT</div>
</aside>

<aside class="widget connect abs">
  <h3>Quick Connect</h3>
  <div class="social"><span></span><span></span><span></span><span></span></div>
</aside>

<main class="featured abs">
  <div class="tabs">
    <div class="tab"><svg width="25" height="25" viewBox="0 0 25 25"><circle cx="12.5" cy="12.5" r="11.5" fill="none" stroke="#888" stroke-width="1.3"/><rect x="9" y="8" width="7" height="9" fill="none" stroke="#888" stroke-width="1.2"/><rect x="11" y="12" width="3" height="3" fill="#888"/></svg>Featured Auctions</div>
    <div class="tab"><svg width="25" height="25" viewBox="0 0 25 25"><circle cx="12.5" cy="12.5" r="11.5" fill="none" stroke="#888" stroke-width="1.3"/><rect x="9" y="8" width="7" height="9" fill="none" stroke="#888" stroke-width="1.2"/><rect x="11" y="12" width="3" height="3" fill="#888"/></svg>Upcoming Auctions</div>
    <div class="tab"><svg width="25" height="25" viewBox="0 0 25 25"><circle cx="12.5" cy="12.5" r="11.5" fill="none" stroke="#888" stroke-width="1.3"/><rect x="9" y="8" width="7" height="9" fill="none" stroke="#888" stroke-width="1.2"/><rect x="11" y="12" width="3" height="3" fill="#888"/></svg>Past Auctions</div>
  </div>

  <article class="listing one abs">
    <div class="photo abs" role="img" aria-label="Photo of a white stucco home with palm trees"></div>
    <div class="info abs">
      <h4>Neque Porro Quisquam</h4>
      <p class="lede">In publishing and graphic design, lorem ipsum is a filler text commonly</p>
      <div class="spec"><span class="k">PROPERTY TYPE</span><span class="c">:</span><span class="v">ONGOING</span></div>
      <div class="spec"><span class="k">LOCATION / AREA</span><span class="c">:</span><span class="v">SENECA, SC 29679</span></div>
      <div class="spec"><span class="k">PRICES</span><span class="c">:</span><span class="v price">$ 18000</span></div>
      <div class="actions"><span>Details</span><span>Photo</span></div>
    </div>
  </article>

  <article class="listing two abs">
    <div class="photo abs" role="img" aria-label="Photo of a white stucco home with palm trees"></div>
    <div class="info abs">
      <h4>Neque Porro Quisquam</h4>
      <p class="lede">In publishing and graphic design, lorem ipsum is a filler text commonly</p>
      <div class="spec"><span class="k">PROPERTY TYPE</span><span class="c">:</span><span class="v">ONGOING</span></div>
      <div class="spec"><span class="k">LOCATION / AREA</span><span class="c">:</span><span class="v">SENECA, SC 29679</span></div>
      <div class="spec"><span class="k">PRICES</span><span class="c">:</span><span class="v price">$ 18000</span></div>
      <div class="actions"><span>Details</span><span>Photo</span></div>
    </div>
  </article>
</main>

<footer class="site-footer abs">
  <div class="footer-mark abs">Brisko Auctions</div>
  <div class="footer-name abs">Brisko Auctions &amp; Realty, Inc.</div>
  <div class="footer-contact abs">58391 Corvan Hollow Road • Suite 604 • Orlando, FL 32899<br>Office: 407.555.0148 / Cell: 407.555.0193 / Fax: 407.555.0176<br>Email: info@briskoauctions.example</div>
  <div class="badges abs">
    <span style="width:52px;height:36px;border-radius:4px"></span>
    <span style="width:30px;height:36px"></span>
    <span style="width:64px;height:24px"></span>
    <span style="width:26px;height:32px"></span>
  </div>
  <div class="copyright abs">© Copyright 2014, all rights reserved</div>
</footer>
</body>
</html>
```